Consulting firm need a professional powerpoint design

A startup Climate change firm needs a powerpoint template design. The design should reflect aspects of climate change adaptation, resilience and environmental sustainability.

The powerpoint design must convey aspects of nature and climate action for a resilient society.

The last slide of the powerpoint must have a allocation for a slogan such as 'Linking science and decision-making'.

Use the colors in the logo and business card for the powerpoint design.

Target Market(s)

Government and industry

Font styles to use
Sans Serif
Other font styles liked:
• nexa font family

Colors
85cae6
abd037
fece3e

Requirements
Must have
• - Colors used in logo and business card
- Convey science and nature
- Professional
Nice to have
• Many pages
Should not have
• Not complicated

```html
<!DOCTYPE html>
<html lang="en">
<head>
<meta charset="utf-8">
<title>Verdanta – Overview Presentation Template</title>
<link href="https://fonts.googleapis.com/css2?family=Montserrat:wght@300;400;500;600&display=swap" rel="stylesheet">
<style>
  :root {
    --sky: #85cae6;
    --lime: #abd037;
    --sun: #fece3e;
    --teal: #1ab1cc;
    --deep-teal: #22789c;
    --leaf: #6fd36a;
    --ink: #2e3352;
    --muted: #9a9db0;
    --paper: #fbfaff;
    --cream: #fdf4d6;
    --stage: #f3f3f6;
  }
  * { margin: 0; padding: 0; box-sizing: border-box; }
  html, body { width: 900px; height: 1200px; overflow: hidden; }
  body { background: var(--stage); font-family: "Montserrat", sans-serif; color: var(--ink); position: relative; }

  .slide { position: absolute; width: 320px; height: 180px; overflow: hidden; background: var(--paper); box-shadow: 0 4px 14px rgba(0,0,0,.12); }
  .col-left { left: 93px; } .col-right { left: 486px; }
  .row-1 { top: 20px; } .row-2 { top: 216px; } .row-3 { top: 412px; }
  .row-4 { top: 608px; } .row-5 { top: 804px; } .row-6 { top: 1000px; }

  .block, .photo { position: absolute; }
  .title { position: absolute; font-weight: 500; font-size: 12px; line-height: 1.3; color: var(--ink); }
  .fine { position: absolute; font-weight: 300; font-size: 3.4px; line-height: 1.6; color: var(--muted); }
  .fine.justify { text-align: justify; }

  .mark { position: absolute; display: flex; align-items: center; gap: 2px; }
  .mark-dot { width: 7px; height: 7px; border-radius: 50%; background: var(--teal); }
  .mark-name { font-weight: 600; font-size: 5px; letter-spacing: .4px; color: var(--ink); }

  /* 1 Cover */
  .cover-photo { inset: 0; background: linear-gradient(180deg, #7a6e6a 0%, #b9826a 35%, #f29a4a 62%, #f7c35a 70%, #8aa86a 78%, #9ec36b 100%); }
  .cover-strip { left: 274px; top: 0; width: 46px; height: 155px; background: rgba(220,190,80,.85); }
  .cover .mark { left: 110px; top: 78px; gap: 4px; }
  .cover .mark-dot { width: 20px; height: 20px; background: var(--sun); }
  .cover .mark-name { font-size: 15px; color: #ffffff; letter-spacing: 1px; }
  .cover-slogan { position: absolute; left: 134px; top: 100px; font-size: 5.4px; color: #ffffff; }
  .cover-title { position: absolute; left: 0; width: 320px; top: 146px; text-align: center; font-weight: 600; font-size: 12px; color: #fff; }
  .cover-client { position: absolute; left: 0; width: 320px; top: 163px; text-align: center; font-size: 5px; color: #fff; }

  /* 2 Welcome */
  .welcome-photo { inset: 0; background: linear-gradient(135deg, #eeeeee, #d4d4d4 60%, #e6e6e6); }
  .welcome-top { left: 124px; top: 0; width: 130px; height: 180px; background: var(--leaf); opacity: .95; }
  .welcome-box { left: 58px; top: 33px; width: 196px; height: 114px; background: var(--leaf); }
  .welcome-side { left: 254px; top: 0; width: 66px; height: 180px; background: #ffffff; }
  .welcome-title { position: absolute; left: 93px; top: 52px; font-weight: 500; font-size: 12px; color: #fff; }
  .welcome .fine { left: 93px; top: 72px; width: 138px; color: #f1fbef; }
  .welcome-vertical { position: absolute; left: 276px; top: 20px; writing-mode: vertical-rl; font-weight: 500; font-size: 13px; color: var(--lime); }

  /* 3 We are */
  .weare-photo-a { left: 171px; top: 0; width: 83px; height: 118px; background: linear-gradient(160deg, #7e8a6a, #4e7d3e 40%, #6e6bb8 75%, #e8c23a); }
  .weare-photo-b { left: 171px; top: 118px; width: 83px; height: 62px; background: linear-gradient(180deg, #3f7a2f, #2e5a22 55%, #a04a2a); }
  .weare-blue { left: 254px; top: 0; width: 66px; height: 180px; background: var(--sky); }
  .weare .title { left: 26px; top: 36px; }
  .weare .fine { left: 26px; top: 56px; width: 118px; }
  .weare-note { position: absolute; left: 267px; width: 40px; font-size: 3.6px; line-height: 1.9; color: #fff; font-weight: 300; }

  /* 4 Quote */
  .quote-photo { inset: 0; background: linear-gradient(180deg, #1d2e44, #3a5870 40%, #2c4a5a); }
  .quote-strip { left: 0; top: 0; width: 28px; height: 180px; background: var(--sun); }
  .quote-box { left: 28px; top: 24px; width: 264px; height: 156px; background: rgba(240,200,60,.88); }
  .quote-text { position: absolute; left: 57px; top: 46px; width: 210px; font-weight: 500; font-size: 10.5px; line-height: 1.38; color: var(--ink); }
  .quote .mark { left: 176px; top: 140px; }
  .quote .mark-dot { width: 12px; height: 12px; background: var(--lime); }
  .quote .mark-name { font-size: 7px; }

  /* 5 Profile */
  .profile .title { left: 30px; top: 35px; }
  .profile .fine.col-a { left: 30px; top: 55px; width: 128px; }
  .profile .fine.col-b { left: 200px; top: 55px; width: 98px; }
  .profile-blue { left: 0; top: 89px; width: 67px; height: 91px; background: var(--sky); }
  .profile-photo { left: 67px; top: 89px; width: 235px; height: 91px; background: linear-gradient(160deg, #1c3f8e, #2b57b0 45%, #5f7fbf 60%, #163682); }

  /* 6 Help everyone */
  .help-blue { left: 0; top: 0; width: 112px; height: 146px; background: var(--sky); }
  .help-strip { left: 112px; top: 0; width: 19px; height: 71px; background: var(--deep-teal); }
  .help-base { left: 0; top: 127px; width: 93px; height: 19px; background: var(--deep-teal); }
  .help-photo-a { left: 28px; top: 25px; width: 84px; height: 103px; background: linear-gradient(180deg, #cfd8de, #6d8aa5 45%, #1f4c8c); }
  .help-photo-b { left: 93px; top: 71px; width: 67px; height: 84px; background: linear-gradient(160deg, #1f2f3a, #8a9aa2 50%, #14212b); }
  .help .title { left: 187px; top: 30px; }
  .help-item { position: absolute; left: 187px; width: 100px; }
  .help-item h3 { font-weight: 600; font-size: 4.6px; color: var(--muted); margin-bottom: 2px; }
  .help-item p { font-weight: 300; font-size: 3.4px; line-height: 1.6; color: var(--muted); }

  /* 7 Rational benefits */
  .benefit-photo { left: 0; top: 28px; width: 85px; height: 123px; background: linear-gradient(180deg, #4e6c86, #9fb3c4 50%, #3f6b3f); }
  .benefit-box { left: 85px; top: 28px; width: 170px; height: 123px; background: linear-gradient(180deg, #9fce5c, #86bd4a 70%, #6ea83a); }
  .benefit-lime { left: 255px; top: 28px; width: 65px; height: 123px; background: var(--lime); }
  .benefit-title { position: absolute; left: 112px; top: 48px; font-weight: 500; font-size: 12px; line-height: 1.3; color: #fff; }
  .benefit-list { position: absolute; left: 112px; top: 82px; width: 130px; list-style: none; font-size: 5.8px; line-height: 2; color: #fff; }

  /* 8 Create value */
  .value { background: var(--cream); }
  .value-photo { left: 0; top: 24px; width: 140px; height: 132px; background: radial-gradient(circle at 50% 55%, #b5e36a, #7cc23a 50%, #5e9a2b); }
  .value-panel { left: 193px; top: 0; width: 127px; height: 180px; background: var(--sun); }
  .value .title { left: 217px; top: 33px; }
  .value .fine { left: 217px; top: 68px; width: 82px; color: #8c7740; }
  .value-list { position: absolute; left: 224px; top: 90px; width: 78px; font-weight: 300; font-size: 3.4px; line-height: 1.6; color: #8c7740; }

  /* 9 About */
  .about-cap { left: 214px; top: 0; width: 106px; height: 28px; background: var(--teal); }
  .about-foot { left: 214px; top: 151px; width: 106px; height: 29px; background: var(--teal); }
  .about-photo { left: 159px; top: 28px; width: 161px; height: 123px; background: linear-gradient(180deg, #14283f, #b7d2e4 35%, #e9f3f8 50%, #4d7593 70%, #1d3a50); }
  .about .title { left: 18px; top: 53px; }
  .about .fine { left: 18px; top: 73px; width: 131px; }
  .about .mark-name { color: #fff; }
  .about .mark-dot { background: var(--sun); }

  /* 10 Landscape */
  .land-photo { left: 0; top: 0; width: 320px; height: 128px; background: linear-gradient(180deg, #3c5670, #8ea4b6 35%, #3d6a3a 65%, #5ea33c); }
  .land .mark { left: 44px; top: 146px; gap: 4px; }
  .land .mark-dot { width: 12px; height: 12px; background: var(--sun); }
  .land .mark-name { font-size: 8px; }
  .land .fine { left: 140px; top: 141px; width: 135px; }

  .tri-bar { position: absolute; left: 0; bottom: 0; width: 320px; height: 3px; display: flex; }
  .tri-bar span { flex: 1; }
  .tri-bar .c1 { background: var(--sun); } .tri-bar .c2 { background: var(--teal); } .tri-bar .c3 { background: var(--lime); }

  /* 11 Portfolio */
  .folio-strip { left: 0; top: 0; width: 44px; height: 180px; background: var(--lime); }
  .folio-grid { position: absolute; left: 47px; top: 27px; width: 171px; height: 126px; display: grid; grid-template-columns: repeat(3, 1fr); gap: 3px; }
  .folio-grid .tile { width: 100%; height: 100%; }
  .t1 { background: linear-gradient(180deg, #4e6c86, #a3b5c4 50%, #3f6b3f); }
  .t2 { background: linear-gradient(180deg, #3f7a2f, #2e5a22 60%, #a04a2a); }
  .t3 { background: linear-gradient(160deg, #7e8a6a, #4e7d3e 40%, #6e6bb8 75%, #e8c23a); }
  .t4 { background: linear-gradient(180deg, #e2e8e6, #4c6b4a 45%, #2a4a44); }
  .t5 { background: linear-gradient(160deg, #4e7d3e, #6e6bb8 60%, #e8c23a); }
  .t6 { background: radial-gradient(circle at 50% 55%, #b5e36a, #7cc23a 55%, #5e9a2b); }
  .folio .title { left: 233px; top: 33px; }
  .folio-list { position: absolute; left: 233px; top: 72px; width: 70px; font-weight: 300; font-size: 3.5px; line-height: 1.7; color: var(--muted); padding-left: 8px; }

  /* 12 Closing */
  .close-ring { position: absolute; left: 25px; top: 27px; width: 130px; height: 130px; }
  .close .title { left: 193px; top: 37px; }
  .close-item { position: absolute; left: 193px; width: 108px; }
  .close-item h3 { font-weight: 500; font-size: 5.3px; color: var(--muted); margin-bottom: 1.5px; }
  .close-item p { font-weight: 300; font-size: 3.4px; line-height: 1.5; color: var(--muted); }

  .mark.top-left { left: 24px; top: 7px; }
  .mark.top-right { right: 18px; top: 7px; }
</style>
</head>
<body>

<!-- 1 Cover -->
<section class="slide cover col-left row-1">
  <div class="photo cover-photo" role="img" aria-label="Wind turbines in a green field at sunset"></div>
  <div class="block cover-strip"></div>
  <div class="mark"><span class="mark-dot"></span><span class="mark-name">VERDANTA</span></div>
  <p class="cover-slogan">Linking science and decision-making</p>
  <h1 class="cover-title">Overview Presentation</h1>
  <p class="cover-client">The Client Name Here</p>
</section>

<!-- 2 Welcome -->
<section class="slide welcome col-right row-1">
  <div class="photo welcome-photo" role="img" aria-label="Black and white photo of a meeting room with a flip chart"></div>
  <div class="block welcome-top"></div>
  <div class="block welcome-box"></div>
  <div class="block welcome-side"></div>
  <div class="mark top-left"><span class="mark-dot"></span><span class="mark-name">VERDANTA</span></div>
  <h2 class="welcome-title">Welcome</h2>
  <p class="fine">Our team turns climate research into clear guidance for leaders who plan for a changing world. We help cities and industry adapt early and build lasting resilience.</p>
  <p class="welcome-vertical">Hello Verdanta</p>
</section>

<!-- 3 We are -->
<section class="slide weare col-left row-2">
  <div class="mark top-left"><span class="mark-dot"></span><span class="mark-name">VERDANTA</span></div>
  <h2 class="title">We Are Verdanta</h2>
  <p class="fine justify">We bring climate science, data and field experience together so decision makers can act with confidence. From flood risk to heat planning, our advisers map the threats, weigh the options and design practical measures that protect people, assets and ecosystems. We work alongside government agencies and companies, building shared evidence and tools that stay useful long after a project ends. Every study is grounded in peer reviewed research and shaped by local knowledge.</p>
  <div class="photo weare-photo-a" role="img" aria-label="Green roof planted with purple flowers"></div>
  <div class="photo weare-photo-b" role="img" aria-label="Hedge wall growing above red brick"></div>
  <div class="block weare-blue"></div>
  <p class="weare-note" style="top:46px">We think about every level of risk</p>
  <p class="weare-note" style="top:136px">We think about every level of risk</p>
</section>

<!-- 4 Quote -->
<section class="slide quote col-right row-2">
  <div class="photo quote-photo" role="img" aria-label="Glacier front meeting dark water"></div>
  <div class="block quote-strip"></div>
  <div class="block quote-box"></div>
  <p class="quote-text">“Climate change is real. It is happening right now, it is the most urgent threat facing our entire species and we need to work collectively together and stop procrastinating.”</p>
  <div class="mark"><span class="mark-dot"></span><span class="mark-name">VERDANTA</span></div>
</section>

<!-- 5 Profile -->
<section class="slide profile col-left row-3">
  <div class="mark top-left"><span class="mark-dot"></span><span class="mark-name">VERDANTA</span></div>
  <h2 class="title">Profile</h2>
  <p class="fine col-a">We think about every level of climate risk, which is another way of saying every place where people meet a changing environment.</p>
  <p class="fine col-b">Our studies cover water, heat and land use, giving planners a clear view of what lies ahead.</p>
  <div class="block profile-blue"></div>
  <div class="photo profile-photo" role="img" aria-label="Whale surfacing in deep blue ocean"></div>
</section>

<!-- 6 Help everyone -->
<section class="slide help col-right row-3">
  <div class="block help-blue"></div>
  <div class="block help-strip"></div>
  <div class="block help-base"></div>
  <div class="photo help-photo-a" role="img" aria-label="Researchers working on a ship deck at sea"></div>
  <div class="photo help-photo-b" role="img" aria-label="Sunlight on the ocean surface with floating ice"></div>
  <div class="mark top-right"><span class="mark-dot"></span><span class="mark-name">VERDANTA</span></div>
  <h2 class="title">Help<br>everyone</h2>
  <div class="help-item" style="top:68px"><h3>Your Text Here</h3><p>We think about every level of risk and how each one shapes a plan</p></div>
  <div class="help-item" style="top:99px"><h3>Your Text Here</h3><p>We think about every level of risk and how each one shapes a plan</p></div>
  <div class="help-item" style="top:130px"><h3>Your Text Here</h3><p>We think about every level of risk and how each one shapes a plan</p></div>
</section>

<!-- 7 Rational benefits -->
<section class="slide benefit col-left row-4">
  <div class="mark top-right"><span class="mark-dot"></span><span class="mark-name">VERDANTA</span></div>
  <div class="photo benefit-photo" role="img" aria-label="Misty forested mountain under cloudy sky"></div>
  <div class="photo benefit-box" role="img" aria-label="Misty forest with green tint"></div>
  <div class="block benefit-lime"></div>
  <h2 class="benefit-title">Rational<br>Benefits:</h2>
  <ul class="benefit-list">
    <li>- Simplicity in complex world of value</li>
    <li>- Clarity</li>
    <li>- Easy access - low deployment threshold</li>
  </ul>
</section>

<!-- 8 Create value -->
<section class="slide value col-right row-4">
  <div class="photo value-photo" role="img" aria-label="Hands holding fresh lettuce in a hydroponic farm"></div>
  <div class="block value-panel"></div>
  <div class="mark top-right"><span class="mark-dot"></span><span class="mark-name">VERDANTA</span></div>
  <h2 class="title">We can<br>create value</h2>
  <p class="fine">We turn complex data into choices that leaders can use today.</p>
  <ul class="value-list">
    <li>Clear evidence for every decision</li>
    <li>Local knowledge built into models</li>
    <li>Practical steps that cut risk</li>
    <li>Results shared in plain language</li>
  </ul>
</section>

<!-- 9 About -->
<section class="slide about col-left row-5">
  <div class="block about-cap"></div>
  <div class="mark top-right"><span class="mark-dot"></span><span class="mark-name">VERDANTA</span></div>
  <h2 class="title">About Verdanta</h2>
  <p class="fine justify">We think about every level of climate risk, which is another way of saying every point where communities meet a changing environment. Our advisers combine research, modelling and local insight to shape adaptation plans that work. Then we stay involved, tracking results and refining each measure as conditions shift over time.</p>
  <div class="photo about-photo" role="img" aria-label="Blue glacier wall above calm water"></div>
  <div class="block about-foot"></div>
</section>

<!-- 10 Landscape -->
<section class="slide land col-right row-5">
  <div class="photo land-photo" role="img" aria-label="Misty pine forest on a mountain slope"></div>
  <div class="mark"><span class="mark-dot"></span><span class="mark-name">VERDANTA</span></div>
  <p class="fine">Healthy forests, clean water and stable climates depend on choices made today. We help leaders see the evidence and act on it with confidence and care.</p>
  <div class="tri-bar"><span class="c1"></span><span class="c2"></span><span class="c3"></span></div>
</section>

<!-- 11 Portfolio -->
<section class="slide folio col-left row-6">
  <div class="block folio-strip"></div>
  <div class="folio-grid">
    <div class="tile t1" role="img" aria-label="Misty forest"></div>
    <div class="tile t2" role="img" aria-label="Hedge above brick wall"></div>
    <div class="tile t3" role="img" aria-label="Green roof with flowers"></div>
    <div class="tile t4" role="img" aria-label="Trees reflected in a lake"></div>
    <div class="tile t5" role="img" aria-label="Flowering green roof detail"></div>
    <div class="tile t6" role="img" aria-label="Fresh lettuce crop"></div>
  </div>
  <div class="mark top-right"><span class="mark-dot"></span><span class="mark-name">VERDANTA</span></div>
  <h2 class="title">Portfolio<br>images</h2>
  <ol class="folio-list">
    <li>Forest recovery study</li>
    <li>Urban green walls</li>
    <li>Wetland planting trial</li>
    <li>Coastal habitat survey</li>
    <li>River basin review</li>
    <li>Vertical farm pilot</li>
  </ol>
</section>

<!-- 12 Closing -->
<section class="slide close col-right row-6">
  <svg class="close-ring" viewBox="0 0 130 130" aria-hidden="true">
    <g fill="none" stroke-width="30">
      <path d="M65 20 A45 45 0 0 1 104 87.5" stroke="#fece3e"/>
      <path d="M104 87.5 A45 45 0 0 1 26 87.5" stroke="#85cae6"/>
      <path d="M26 87.5 A45 45 0 0 1 65 20" stroke="#abd037"/>
    </g>
  </svg>
  <div class="mark top-right"><span class="mark-dot"></span><span class="mark-name">VERDANTA</span></div>
  <h2 class="title">Place your text<br>title here</h2>
  <div class="close-item" style="top:78px"><h3>Simplicity in complex world of value</h3><p>Clear science shaped into steps anyone can follow.</p></div>
  <div class="close-item" style="top:105px"><h3>Clarity</h3><p>Findings explained in plain and direct language.</p></div>
  <div class="close-item" style="top:134px"><h3>Easy access - low deployment</h3><p>Tools that teams can adopt without delay.</p></div>
  <div class="tri-bar"><span class="c1"></span><span class="c2"></span><span class="c3"></span></div>
</section>

</body>
</html>
```